Business Card Design

We sell fish products to corporate food companies who then turn these products into final food products for consumers

Industry/Entity Type

Business

Contact Information for Business Card

I need a corporate business card template for a fish products business. We would like it be professional for use in dealing with multi national companies. This company business card template will be used by multiple employees so the following fields must be open to edit (Name, Phone Number and Email address)

```html
<!DOCTYPE html>
<html lang="en">
<head>
<meta charset="utf-8">
<title>Coral Bay Seafoods – Business Card</title>
<link href="https://fonts.googleapis.com/css2?family=Lato:wght@400;700;900&display=swap" rel="stylesheet">
<style>
  :root {
    --backdrop: #2a2a2a;
    --band-blue: #0d5aa7;
    --band-blue-deep: #0a4f95;
    --card-white: #f4f4f4;
    --accent-green: #5cc08a;
    --brand-blue: #0d4f9a;
    --text-light: #e8eef6;
  }
  * { margin: 0; padding: 0; box-sizing: border-box; }
  html, body {
    width: 1200px;
    height: 873px;
    overflow: hidden;
    background: var(--backdrop);
    font-family: "Lato", sans-serif;
  }
  .stage {
    width: 1200px;
    height: 873px;
    display: flex;
    align-items: center;
    justify-content: center;
  }
  .card {
    width: 470px;
    height: 760px;
    border-radius: 26px;
    overflow: hidden;
    background: var(--card-white);
    display: flex;
    flex-direction: column;
    box-shadow: 0 20px 40px rgba(0,0,0,0.45);
  }
  .card__header {
    height: 150px;
    background: var(--band-blue);
    display: flex;
    flex-direction: column;
    align-items: center;
    justify-content: center;
    gap: 6px;
  }
  .holder-name {
    color: var(--accent-green);
    font-weight: 900;
    font-size: 34px;
    letter-spacing: 0.2px;
  }
  .holder-title {
    color: var(--text-light);
    font-weight: 700;
    font-size: 16px;
    letter-spacing: 0.5px;
  }
  .card__brand {
    flex: 1;
    display: flex;
    align-items: center;
    justify-content: center;
    gap: 14px;
  }
  .brand-dot {
    width: 34px;
    height: 34px;
    border-radius: 50%;
    background: var(--brand-blue);
  }
  .brand-name {
    color: var(--brand-blue);
    font-weight: 700;
    font-size: 34px;
    line-height: 1.1;
    text-align: left;
  }
  .card__contact {
    height: 265px;
    background: var(--band-blue);
    display: flex;
    flex-direction: column;
    align-items: center;
    padding-top: 44px;
    gap: 30px;
  }
  .contact-icons {
    display: flex;
    gap: 26px;
  }
  .contact-icons svg { width: 28px; height: 22px; }
  .contact-lines {
    display: flex;
    flex-direction: column;
    align-items: center;
    gap: 22px;
    color: var(--text-light);
    font-weight: 700;
    font-size: 21px;
  }
</style>
</head>
<body>
  <main class="stage">
    <article class="card">
      <header class="card__header">
        <h1 class="holder-name">Marco Delgado</h1>
        <p class="holder-title">INCHARGE</p>
      </header>

      <section class="card__brand">
        <span class="brand-dot" aria-hidden="true"></span>
        <span class="brand-name">Coral Bay<br>Seafoods</span>
      </section>

      <footer class="card__contact">
        <div class="contact-icons">
          <svg viewBox="0 0 28 22" aria-label="Phone">
            <path d="M4 8 Q14 0 24 8 L21 11 L18 8 L10 8 L7 11 Z" fill="var(--accent-green)"/>
            <rect x="7" y="11" width="14" height="9" rx="1.5" fill="var(--accent-green)"/>
            <circle cx="14" cy="15.5" r="2.2" fill="var(--band-blue)"/>
          </svg>
          <svg viewBox="0 0 28 22" aria-label="Email">
            <rect x="2" y="3" width="24" height="16" rx="1" fill="var(--accent-green)"/>
            <path d="M2.5 4 L14 13 L25.5 4" fill="none" stroke="var(--band-blue)" stroke-width="1.6"/>
          </svg>
        </div>
        <div class="contact-lines">
          <p class="contact-phone">+61 300 555 120/+61 400 555 782</p>
          <p class="contact-email">hello@coralbayseafoods.com</p>
        </div>
      </footer>
    </article>
  </main>
</body>
</html>
```